FREE Network Assessment image for landing page

This graphic will be on a landing page and on the left will be Text and a download button that we change and control. The graphic for this project will be to the right.
I will add an example of the landing page area so that it makes more sense.

Please include the text from the sample - the font needs to be the same style as what we are using on the left side!

The graphic needs to be a .png file, roughly 713 x 527 white background. Use discretion on design layout.

Colors are black, Red = PMS 1795 and Gray = Cool Gray 10

Thanks,
Tom Farrow

Target Market(s)

small businesses

Industry/Entity Type

Information Technology

Font styles to use
Other font styles liked:
• See sample

Requirements
Must have
• see description
Nice to have
• Possibly small technology related image to help enhance the text but I don't want any image to compete with the text. Keep in mind the colors mentioned in the description - this is the web site colors.
Should not have
• Should not be hard to read

```html
<!DOCTYPE html>
<html lang="en">
<head>
<meta charset="utf-8">
<title>Free Network &amp; Computer Health Check Service</title>
<link rel="stylesheet" href="https://fonts.googleapis.com/css2?family=Bebas+Neue&family=Noto+Sans:wght@400;600&display=swap">
<style>
  :root {
    --brand-red: #d22630;
    --cool-gray: #5b6670;
    --paper: #ffffff;
    --map-light: #eef0f2;
    --map-mid: #d9dde1;
  }
  * { margin: 0; padding: 0; box-sizing: border-box; }
  html, body {
    width: 1200px;
    height: 887px;
    overflow: hidden;
    background: var(--paper);
  }
  .promo {
    position: relative;
    width: 1200px;
    height: 887px;
    background: var(--paper);
  }
  .promo__title {
    position: absolute;
    left: 46px;
    top: 40px;
    font-family: "Bebas Neue", "Oswald", sans-serif;
    font-weight: 400;
    font-size: 82px;
    line-height: 73px;
    letter-spacing: 5px;
    color: var(--cool-gray);
  }
  .promo__benefits {
    position: absolute;
    left: 46px;
    top: 292px;
    width: 700px;
    list-style: none;
    font-family: "Noto Sans", "Verdana", sans-serif;
    font-size: 25px;
    line-height: 30px;
    letter-spacing: 0.6px;
    color: var(--brand-red);
  }
  .promo__benefit { margin-bottom: 33px; }
  .promo__benefit:nth-child(2) { margin-bottom: 36px; }
  .promo__cta {
    position: absolute;
    left: 40px;
    top: 783px;
    width: 507px;
    height: 64px;
    border-radius: 32px;
    background: var(--brand-red);
    color: var(--paper);
    font-family: "Noto Sans", "Verdana", sans-serif;
    font-weight: 600;
    font-size: 28px;
    letter-spacing: 2px;
    display: flex;
    align-items: center;
    justify-content: center;
    text-decoration: none;
  }
  .promo__illustration {
    position: absolute;
    left: 631px;
    top: 290px;
    width: 530px;
    height: 350px;
    border-radius: 40px;
    background: radial-gradient(ellipse at 45% 50%, var(--map-mid) 0%, var(--map-light) 60%, var(--paper) 100%);
  }
</style>
</head>
<body>
  <main class="promo">
    <h1 class="promo__title">Free Network &amp;<br>Computerhealth<br>Check Service</h1>

    <ul class="promo__benefits">
      <li class="promo__benefit">Check your network’s security against<br>hacker attacks, theft, ransomware,<br>viruses, and more.</li>
      <li class="promo__benefit">See who and what has access to your<br>network and data.</li>
      <li class="promo__benefit">Perform network and Internet speed<br>test</li>
      <li class="promo__benefit">Resolve PC slowness issues, security<br>vulnerabilities and improper configurations</li>
      <li class="promo__benefit">Validate your backups are working<br>and recoverable in a timely fashion.</li>
    </ul>

    <div class="promo__illustration" role="img" aria-label="Illustration of a laptop with gears on a world map, surrounded by technology icons such as email, location pin, folder, globe and chart"></div>

    <a class="promo__cta" href="#book">Book an appointment now!</a>
  </main>
</body>
</html>
```